Toravelle Works Luxury Candles

Luxury box design,, simple and sophisticated look,,

My collection of candles come in 5 different fragrances, i would like to be able to change the fragrance name on the boxes,,,,

I would like the outline of australia on the front down the bottom , (only small) to represent this is an australian product.

My boxes are white gloss,,,

Happy for you to use my current logo ,,, however you'll have to change Toravelle Nails to Toravelle Works.

```html
<!DOCTYPE html>
<html lang="en">
<head>
<meta charset="utf-8">
<title>Toravelle Works Luxury Candles – Vanilla Caramel Box</title>
<link rel="stylesheet" href="https://fonts.googleapis.com/css2?family=Zilla+Slab:wght@300;400&display=swap">
<style>
  :root {
    --page-bg: #ffffff;
    --marble-white: #f6f7f9;
    --marble-grey: #dfe2e7;
    --marble-vein: #b9bcc2;
    --gold: #c9a02a;
    --gold-light: #e3c35a;
    --ink: #55585f;
    --label-bg: #ffffff;
    --map-grey: #dde2e8;
  }
  * { box-sizing: border-box; margin: 0; padding: 0; }
  html, body {
    width: 1200px;
    height: 960px;
    overflow: hidden;
    background: var(--page-bg);
  }
  body {
    font-family: "Zilla Slab", Georgia, serif;
    color: var(--ink);
  }
  .canvas {
    position: relative;
    width: 1200px;
    height: 960px;
  }
  .box-panel {
    position: absolute;
    top: 168px;
    width: 456px;
    height: 646px;
    overflow: hidden;
  }
  .box-panel--front { left: 62px; }
  .box-panel--back { left: 628px; }
  .marble-surface {
    position: absolute;
    inset: 0;
    background:
      radial-gradient(ellipse at 30% 20%, var(--marble-grey) 0%, transparent 35%),
      radial-gradient(ellipse at 75% 65%, var(--marble-grey) 0%, transparent 40%),
      linear-gradient(155deg, var(--marble-white) 0%, #eef0f3 30%, #fbf6e6 55%, var(--marble-white) 75%, #efe6c9 100%);
  }
  .label {
    position: absolute;
    left: 67px;
    width: 299px;
    background: var(--label-bg);
    border: 3px solid var(--gold);
    text-align: center;
  }
  .label--front {
    top: 187px;
    height: 272px;
    padding-top: 44px;
  }
  .label--back {
    top: 91px;
    height: 462px;
    padding: 34px 20px 0;
  }
  .brand-name {
    font-size: 27px;
    font-weight: 300;
    color: var(--ink);
    letter-spacing: 0.5px;
  }
  .fragrance-name {
    color: var(--gold);
    font-weight: 400;
    letter-spacing: 0.5px;
  }
  .label--front .fragrance-name {
    font-size: 27px;
    margin-top: 50px;
  }
  .label--back .fragrance-name {
    font-size: 18px;
    margin-bottom: 22px;
  }
  .net-weight {
    font-size: 13px;
    margin-top: 40px;
  }
  .product-claims {
    font-size: 11.5px;
    line-height: 1.4;
    margin-top: 6px;
  }
  .description {
    font-size: 13.2px;
    line-height: 1.42;
    margin-bottom: 18px;
  }
  .producer {
    position: absolute;
    left: 0;
    right: 0;
    bottom: 34px;
    font-size: 13px;
    line-height: 1.4;
  }
  .origin-mark {
    position: absolute;
    left: 324px;
    top: 520px;
    width: 72px;
    height: 68px;
  }
</style>
</head>
<body>
<main class="canvas">

  <section class="box-panel box-panel--front">
    <div class="marble-surface" role="img" aria-label="White marble texture with grey veins and flowing gold dotted lines"></div>
    <div class="label label--front">
      <p class="brand-name">Toravelle Works</p>
      <h1 class="fragrance-name">VANILLA CARAMEL</h1>
      <p class="net-weight">11 oz.</p>
      <p class="product-claims">hand-poured made with 100% wax<br>natural soy candle made with fine fragrances</p>
    </div>
    <svg class="origin-mark" viewBox="0 0 72 68" role="img" aria-label="Small outline map of Australia in light grey">
      <rect x="0" y="0" width="72" height="68" rx="14" fill="var(--map-grey)"/>
    </svg>
  </section>

  <section class="box-panel box-panel--back">
    <div class="marble-surface" role="img" aria-label="White marble texture with grey veins and flowing gold dotted lines"></div>
    <div class="label label--back">
      <h2 class="fragrance-name">VANILLA CARAMEL</h2>
      <p class="description">Lorem ipsum dolor sit amet, consec-tetuer adipiscing elit, sed diam nonummy nibh euismod tincidunt ut laoreet dolore magna aliquam erat volutpat. Ut wisi enim ad</p>
      <p class="description">Lorem ipsum dolor sit amet, consec-tetuer adipiscing elit, sed diam nonummy nibh euismod tincidunt ut laoreet dolore magna aliquam erat volutpat. Ut wisi enim ad Lorem ipsum dolor sit amet, consec</p>
      <p class="producer">Produced by<br>TORAVELLE WORKS<br>MADE IN AUSTRALIA</p>
    </div>
  </section>

</main>
</body>
</html>
```